Landscape Contractor in need of New Web Design

HELP.. Please Help!!!!. Our current website is old, outdated, ugly... and well nothing like us.... so we are looking for someone to help build a new website that fits our company direction. We are a landscape company with multiple locations in order to meet the needs of our clients and their projects throughout the midwest. When most people think of landscaping, they think of mowing grandmas yard, but that is NOT even remotely close to what we do. We are 100% a commercial landscape company meaning we complete landscape and irrigation services for large scale commercial projects. We are looking for a website to showcase our commercial talents and awesome team of people.
Updates

Address of current website is www.plovermeadowco.com

```html
<!DOCTYPE html>
<html lang="en">
<head>
<meta charset="utf-8">
<title>Plover Meadow — Commercial Landscape Services</title>
<link href="https://fonts.googleapis.com/css2?family=Roboto:wght@400;500;700&family=Roboto+Condensed:wght@700&display=swap" rel="stylesheet">
<style>
:root{
  --green:#4b8a1d;
  --green-dark:#3a6e14;
  --green-band:#3f7a18;
  --lime:#7dbb2a;
  --ink:#222;
  --muted:#666;
  --line:#d8d8d8;
  --footer:#262626;
  --footer-bottom:#1c1c1c;
  --white:#fff;
}
*{box-sizing:border-box;margin:0;padding:0}
html,body{width:1200px;height:5220px;overflow:hidden}
body{font-family:"Roboto",Arial,sans-serif;color:var(--ink);background:var(--white);position:relative}
.heading{font-family:"Roboto Condensed","Arial Narrow",sans-serif;font-weight:700;text-transform:uppercase;text-align:center;font-size:36px;letter-spacing:1px}
.heading::after{content:"";display:block;width:60px;height:3px;background:var(--green);margin:14px auto 0}
.btn{display:inline-block;background:var(--green);color:var(--white);font-size:13px;font-weight:700;text-transform:uppercase;padding:12px 26px;border-radius:22px}

/* header */
.topbar{position:absolute;top:0;left:190px;right:280px;height:44px;display:flex;align-items:center;justify-content:space-between;font-size:13px;color:var(--muted)}
.socials{display:flex;gap:8px;align-items:center}
.socials span{width:22px;height:22px;border-radius:3px;background:var(--green)}
.socials span:nth-child(2){background:#2d9ce0}
.socials span:nth-child(3){background:#2a6fb0}
.payment{margin-left:18px}
.brand{position:absolute;top:18px;left:100px;width:150px;height:100px;display:flex;align-items:center;justify-content:center;gap:8px}
.brand-dot{width:16px;height:16px;border-radius:50%;background:var(--lime)}
.brand-name{font-size:22px;font-weight:700;color:var(--green)}
.nav{position:absolute;top:80px;left:330px;display:flex;gap:34px;font-size:14px;font-weight:700;text-transform:uppercase}
.nav a{color:var(--ink);text-decoration:none;padding-bottom:8px}
.nav a.active{color:var(--green);border-bottom:3px solid var(--green)}
.call{position:absolute;top:44px;right:0;width:280px;height:104px;background:#2d2d2d;color:var(--white);display:flex;align-items:center;gap:16px;padding-left:36px}
.call-icon{width:44px;height:44px;border-radius:50%;background:var(--white);display:flex;align-items:center;justify-content:center}
.call small{display:block;font-size:14px}
.call strong{font-size:22px}

/* hero */
.hero{position:absolute;top:150px;left:0;width:1200px;height:670px;background:linear-gradient(180deg,#b9c7cf 0%,#7f9a6a 40%,#5b7b40 70%,#7f8d86 100%)}
.hero-circle{position:absolute;left:410px;top:40px;width:380px;height:380px;border-radius:50%;background:rgba(255,255,255,.4);display:flex;flex-direction:column;align-items:center;justify-content:center;text-align:center}
.hero-circle h1{font-family:"Roboto Condensed",sans-serif;font-size:46px;line-height:1.1;color:var(--white);text-transform:uppercase;text-shadow:0 2px 6px rgba(0,0,0,.4);margin-bottom:22px}
.arrow{position:absolute;top:300px;width:40px;height:40px;background:rgba(0,0,0,.5);display:flex;align-items:center;justify-content:center}
.arrow.left{left:20px}.arrow.right{right:20px}

/* services */
.services{position:absolute;top:820px;left:0;width:1200px;height:800px}
.services .heading{margin-top:110px}
.service-grid{position:absolute;top:190px;left:112px;display:grid;grid-template-columns:repeat(3,310px);gap:22px 12px}
.service{position:relative;height:242px;background:linear-gradient(160deg,#6f9a4d,#3c5f29)}
.service:nth-child(2){background:linear-gradient(160deg,#c9d0d4,#7d8a6f)}
.service:nth-child(4){background:linear-gradient(160deg,#8d8a73,#4f5b3c)}
.service:nth-child(5){background:linear-gradient(160deg,#5e7a5a,#2f4a2a)}
.service:nth-child(6){background:linear-gradient(160deg,#8aa07a,#4b6436)}
.service-label{position:absolute;left:20px;right:20px;bottom:0;height:46px;background:var(--green);color:var(--white);font-size:15px;font-weight:700;text-transform:uppercase;display:flex;align-items:center;justify-content:center}

/* why */
.why{position:absolute;top:1620px;left:0;width:1200px;height:1000px;background:linear-gradient(135deg,var(--green-band),#4d8a22 50%,var(--green-band))}
.why .heading{color:var(--white);margin-top:110px}
.why .heading::after{background:var(--lime)}
.why-grid{position:absolute;top:255px;left:160px;display:grid;grid-template-columns:repeat(3,270px);gap:40px 45px}
.why-card{background:var(--white);height:270px;text-align:center;padding:24px 22px;position:relative}
.why-card:nth-child(n+4){margin-top:130px}
.why-icon{width:78px;height:78px;border-radius:50%;background:var(--lime);margin:0 auto 30px;display:flex;align-items:center;justify-content:center}
.why-card h3{font-size:15px;margin-bottom:12px}
.why-card p{font-size:12px;line-height:1.6;color:var(--muted)}

/* we are */
.we-are{position:absolute;top:2620px;left:0;width:1200px;height:960px}
.we-are .heading{margin-top:110px}
.we-are .intro{text-align:center;font-size:13px;color:var(--muted);margin:20px auto 0;width:520px;line-height:1.6}
.tile{position:absolute;display:flex;flex-direction:column;align-items:center;justify-content:flex-end;padding-bottom:20px}
.tile h4{color:var(--white);font-size:18px;text-transform:uppercase;margin-bottom:14px;text-shadow:0 1px 4px rgba(0,0,0,.6)}
.tile.residential{left:110px;top:240px;width:368px;height:510px;background:linear-gradient(170deg,#a9a28f,#5f7548 60%,#3e5a2f)}
.tile.government{left:490px;top:240px;width:598px;height:304px;background:linear-gradient(170deg,#8d9aa2,#6a6f5e 50%,#4b6b37);align-items:flex-end;padding-right:30px;justify-content:flex-end}
.tile.government .tile-row{display:flex;gap:40px;align-items:center}
.tile.commercial{left:490px;top:556px;width:300px;height:194px;background:linear-gradient(170deg,#6f8fae,#5b6b52 60%,#3e5a2f)}
.tile.sports{left:800px;top:556px;width:288px;height:194px;background:linear-gradient(170deg,#9aa3a8,#4e7e34 60%,#3c6b25)}

/* testimonials */
.testimonials{position:absolute;top:3580px;left:0;width:1200px;height:470px}
.testimonials .photo{position:absolute;left:0;top:0;width:600px;height:470px;background:linear-gradient(160deg,#8faa70,#5d7a48 50%,#7f8a84)}
.testimonials .quote{position:absolute;left:640px;top:20px;width:440px}
.testimonials h2{font-family:"Roboto Condensed",sans-serif;font-size:34px;text-transform:uppercase;padding-bottom:12px;border-bottom:2px solid var(--green);display:inline-block}
.testimonials blockquote{font-size:13px;font-style:italic;line-height:1.6;color:var(--muted);margin-top:24px}
.testimonials .name{margin-top:14px;font-weight:700;font-size:15px}
.testimonials .org{font-weight:700;font-size:13px;color:var(--muted)}
.dots{display:flex;gap:10px;margin-top:22px}
.dots span{width:30px;height:30px;border-radius:50%;background:#222}
.dots span+span{background:var(--green)}

/* quote form */
.quote-section{position:absolute;top:4050px;left:0;width:1200px;height:770px;background:linear-gradient(180deg,#fff 0%,#fff 72%,#cfd9c4 82%,#7f9a60 100%)}
.quote-section .heading{margin-top:90px}
.contact-row{position:absolute;top:200px;left:0;width:1200px;display:flex;justify-content:center;gap:170px}
.contact-item{text-align:center;width:160px}
.contact-icon{width:60px;height:60px;border-radius:50%;border:2px solid var(--green);margin:0 auto 12px;display:flex;align-items:center;justify-content:center}
.contact-item b{display:block;font-size:12px;text-transform:uppercase}
.contact-item span{font-size:11px;color:var(--muted)}
.form{position:absolute;top:340px;left:235px;width:730px;display:grid;grid-template-columns:1fr 1fr;gap:14px 18px}
.field{height:54px;border:1px solid var(--line);background:var(--white);font-size:13px;color:#999;padding:18px 14px}
.field.message{grid-column:1/3;height:150px}
.form .submit{grid-column:1/3;justify-self:center}

/* footer */
.footer{position:absolute;top:4820px;left:0;width:1200px;height:400px;background:var(--footer);color:#ccc}
.footer-cols{display:grid;grid-template-columns:300px 240px 240px 300px;gap:0;padding:70px 110px 0}
.footer h5{color:var(--white);font-size:18px;text-transform:uppercase;margin-bottom:18px}
.footer p,.footer li{font-size:13px;line-height:1.7;list-style:none}
.footer-bottom{position:absolute;bottom:0;left:0;width:1200px;height:80px;background:var(--footer-bottom);display:flex;align-items:center;justify-content:center;font-size:13px}
.to-top{position:absolute;top:-16px;left:570px;background:var(--green);color:var(--white);font-size:11px;padding:6px 12px;border-radius:12px}
</style>
</head>
<body>

<header>
  <div class="topbar">
    <span>Business Hours: 8am - 5pm | Mon - Fri</span>
    <div class="socials"><span></span><span></span><span></span><span class="payment">Make a Payment</span></div>
  </div>
  <div class="brand"><span class="brand-dot"></span><span class="brand-name">Plover Meadow</span></div>
  <nav class="nav">
    <a class="active">Home</a><a>Divisions</a><a>Services</a><a>About Us</a><a>Gallery</a><a>Contact</a>
  </nav>
  <div class="call">
    <div class="call-icon"><svg width="22" height="22" viewBox="0 0 24 24"><path fill="#2d2d2d" d="M6.6 10.8a15 15 0 0 0 6.6 6.6l2.2-2.2c.3-.3.7-.4 1-.2 1.1.4 2.3.6 3.6.6.6 0 1 .4 1 1V20c0 .6-.4 1-1 1A17 17 0 0 1 3 4c0-.6.4-1 1-1h3.5c.6 0 1 .4 1 1 0 1.3.2 2.5.6 3.6.1.3 0 .7-.2 1z"/></svg></div>
    <div><small>Call us Today :</small><strong>205-555-0142</strong></div>
  </div>
</header>

<section class="hero" role="img" aria-label="Landscaped backyard with pool, lawn chairs and trees">
  <div class="hero-circle">
    <h1>Landscape<br>Maintenance<br>Service</h1>
    <span class="btn">Get a Quote</span>
  </div>
  <span class="arrow left"><svg width="14" height="14" viewBox="0 0 14 14"><path d="M9 2 4 7l5 5" stroke="#fff" stroke-width="2" fill="none"/></svg></span>
  <span class="arrow right"><svg width="14" height="14" viewBox="0 0 14 14"><path d="m5 2 5 5-5 5" stroke="#fff" stroke-width="2" fill="none"/></svg></span>
</section>

<section class="services">
  <h2 class="heading">Our Services</h2>
  <div class="service-grid">
    <div class="service" role="img" aria-label="Freshly mowed lawn"><span class="service-label">Maintenance</span></div>
    <div class="service" role="img" aria-label="House with treated lawn"><span class="service-label">Chemical Applications</span></div>
    <div class="service" role="img" aria-label="Sprinkler watering turf"><span class="service-label">Turf Management</span></div>
    <div class="service" role="img" aria-label="Stone retaining wall and patio"><span class="service-label">Hardscaping</span></div>
    <div class="service" role="img" aria-label="Irrigation system in garden"><span class="service-label">Irrigation</span></div>
    <div class="service" role="img" aria-label="Landscaped garden beds"><span class="service-label">Landscaping</span></div>
  </div>
</section>

<section class="why">
  <h2 class="heading">Why Choose Us?</h2>
  <div class="why-grid">
    <div class="why-card"><div class="why-icon"><svg width="36" height="36" viewBox="0 0 24 24"><circle cx="12" cy="10" r="6" fill="none" stroke="#fff" stroke-width="2"/><path d="M8 15l-2 7 6-3 6 3-2-7" fill="none" stroke="#fff" stroke-width="2"/></svg></div><h3>Specialized Company</h3><p>Plover Meadow strives to set the standard for the highest quality lawn and landscape products and services and to exceed our customers' expectations every time.</p></div>
    <div class="why-card"><div class="why-icon"><svg width="36" height="36" viewBox="0 0 24 24"><path d="M12 2 4 5v6c0 5 3.5 9 8 11 4.5-2 8-6 8-11V5z" fill="none" stroke="#fff" stroke-width="2"/><path d="m8 12 3 3 5-6" fill="none" stroke="#fff" stroke-width="2"/></svg></div><h3>Licensed &amp; Insured</h3><p>Rest assured knowing that Plover Meadow is a fully licensed and insured firm with a superior safety rating.</p></div>
    <div class="why-card"><div class="why-icon"><svg width="36" height="36" viewBox="0 0 24 24"><circle cx="6" cy="12" r="2.5" fill="#fff"/><circle cx="18" cy="5" r="2.5" fill="#fff"/><circle cx="18" cy="19" r="2.5" fill="#fff"/><path d="M6 12 18 5M6 12l12 7" stroke="#fff" stroke-width="2"/></svg></div><h3>Dependable Services</h3><p>Communication is highly valued at Plover Meadow. From start to finish our clients will be kept up to date on their project.</p></div>
    <div class="why-card"><div class="why-icon"><svg width="36" height="36" viewBox="0 0 24 24"><rect x="3" y="5" width="18" height="16" rx="2" fill="none" stroke="#fff" stroke-width="2"/><path d="M3 10h18M8 3v4M16 3v4" stroke="#fff" stroke-width="2"/></svg></div><h3>Day Scheduling</h3><p>Contact our office today to schedule an appointment that meets your needs!</p></div>
    <div class="why-card"><div class="why-icon"><svg width="36" height="36" viewBox="0 0 24 24"><circle cx="12" cy="12" r="9" fill="none" stroke="#fff" stroke-width="2"/><circle cx="12" cy="12" r="5" fill="none" stroke="#fff" stroke-width="2"/><circle cx="12" cy="12" r="1.5" fill="#fff"/></svg></div><h3>Free Consultations</h3><p>Call our office to set up a time to meet with one of our qualified professionals. They will walk your property with you to help you plan the project ahead.</p></div>
    <div class="why-card"><div class="why-icon"><svg width="36" height="36" viewBox="0 0 24 24"><path d="M12 3 5 6v6c0 4 3 7.5 7 9 4-1.5 7-5 7-9V6z" fill="none" stroke="#fff" stroke-width="2"/><path d="m12 8 1.2 2.6 2.8.3-2.1 1.9.6 2.8L12 14l-2.5 1.6.6-2.8L8 10.9l2.8-.3z" fill="#fff"/></svg></div><h3>Reputable Company</h3><p>With 25 years of experience in the landscaping construction business, we have built a reputation for superior projects and service.</p></div>
  </div>
</section>

<section class="we-are">
  <h2 class="heading">We Are</h2>
  <p class="intro">Plover Meadow, Inc. is a full service lawn and landscape contractor providing design, installation, and maintenance services.</p>
  <div class="tile residential" role="img" aria-label="Residential garden with shrubs and flowers"><h4>Residential</h4><span class="btn">View Gallery</span></div>
  <div class="tile government" role="img" aria-label="Government building with landscaped beds"><div class="tile-row"><h4>Government</h4><span class="btn">View Gallery</span></div></div>
  <div class="tile commercial" role="img" aria-label="Commercial building with landscaping"><h4>Commercial</h4><span class="btn">View Gallery</span></div>
  <div class="tile sports" role="img" aria-label="Sports field with stadium seating"><h4>Sports Fields</h4><span class="btn">View Gallery</span></div>
</section>

<section class="testimonials">
  <div class="photo" role="img" aria-label="Backyard patio with covered pool and garden"></div>
  <div class="quote">
    <h2>Testimonials</h2>
    <blockquote>I went by the school again this morning and checked the work performed recently. All areas look very nice and it looks like we received more soil under the playground than I expected. I was very pleased with the work performed by Plover Meadow and the cooperation that was on the part of your entire crew. It is a pleasure working with you. Thanks.</blockquote>
    <p class="name">Dale Morrow</p>
    <p class="org">– Eastbrook Valley School District</p>
    <div class="dots"><span></span><span></span></div>
  </div>
</section>

<section class="quote-section">
  <h2 class="heading">Request a Quick Quote</h2>
  <div class="contact-row">
    <div class="contact-item"><div class="contact-icon"><svg width="24" height="24" viewBox="0 0 24 24"><path d="M12 2a7 7 0 0 0-7 7c0 5 7 13 7 13s7-8 7-13a7 7 0 0 0-7-7zm0 9.5A2.5 2.5 0 1 1 12 6.5a2.5 2.5 0 0 1 0 5z" fill="#4b8a1d"/></svg></div><b>Address :</b><span>4410 W Orchard Lane, Millbrook, KS 66000</span></div>
    <div class="contact-item"><div class="contact-icon"><svg width="22" height="22" viewBox="0 0 24 24"><path fill="#4b8a1d" d="M6.6 10.8a15 15 0 0 0 6.6 6.6l2.2-2.2c.3-.3.7-.4 1-.2 1.1.4 2.3.6 3.6.6.6 0 1 .4 1 1V20c0 .6-.4 1-1 1A17 17 0 0 1 3 4c0-.6.4-1 1-1h3.5c.6 0 1 .4 1 1 0 1.3.2 2.5.6 3.6.1.3 0 .7-.2 1z"/></svg></div><b>Phone :</b><span>+1 205-555-0142</span></div>
    <div class="contact-item"><div class="contact-icon"><svg width="24" height="24" viewBox="0 0 24 24"><rect x="3" y="5" width="18" height="14" rx="1" fill="none" stroke="#4b8a1d" stroke-width="2"/><path d="m3 6 9 7 9-7" fill="none" stroke="#4b8a1d" stroke-width="2"/></svg></div><b>Email :</b><span>info@plovermeadowco.com</span></div>
  </div>
  <div class="form">
    <div class="field">First name</div>
    <div class="field">Last name</div>
    <div class="field">Phone</div>
    <div class="field">Email address</div>
    <div class="field message">Message</div>
    <span class="btn submit">Submit</span>
  </div>
</section>

<footer class="footer">
  <div class="footer-cols">
    <div><h5>About Us</h5><p>Plover Meadow strives to set the standard for the highest quality lawn and landscape products and services and to exceed our customers' expectations every time.</p></div>
    <div><h5>Our Services</h5><ul><li>Turf Management</li><li>Hardscaping</li><li>Irrigation</li><li>Landscaping</li></ul></div>
    <div><h5>Quick Links</h5><ul><li>About Us</li><li>Divisions</li><li>Certifications</li><li>Gallery</li></ul></div>
    <div><h5>Contact</h5><p>Plover Meadow Inc. · 4410 W Orchard Lane, Millbrook, KS 66000</p><p style="margin-top:12px">Northside Office : 1 205-555-0142<br>Riverbend Office : 1 205-555-0178</p></div>
  </div>
  <div class="footer-bottom"><span class="to-top">Go top</span>© 2021 Plover Meadow | All Rights Reserved</div>
</footer>

</body>
</html>
```